DJ Poster for events

Poster for bar/club events, advertising the location and date. Example:

Kell Cousins Sports Bar and Tap House presents DJ PIVWHIRL

Friday, July 6th 2012

Bringing you the best in Top 40 - Retro - Funk

"It's gonna be a pivwhirl."

www.thekellcousins.example
clubwall/chirpline: DJ Pivwhirl

portait orientation 8.5x11

require photoshop-ready files to be able to change venue/date info

plimmostock eps material attached may be used

Target Market(s)

clubgoers 21-45

Industry/Entity Type

Advertising

Requirements
Must have
• DJ Pivwhirl logo (provides)
alternatively, create new logo to suit poster style - in which case will commission business cards as well
Nice to have
• venue logo (provided)

photo/cartoon adaptation of dj (headshots provided)

```html
<!DOCTYPE html>
<html lang="en">
<head>
<meta charset="utf-8">
<title>DJ Pivwhirl – Kell Cousins Sports Bar and Tap House</title>
<link rel="stylesheet" href="https://fonts.googleapis.com/css2?family=Anton&family=Pathway+Gothic+One&display=swap">
<style>
  :root {
    --bg-deep: #1c0719;
    --bg-mid: #3a0c34;
    --bg-glow: #5a1550;
    --pink-text: #f4c4e2;
    --pink-soft: #e77ab6;
    --neon: #ff3dbb;
    --band-strong: #c3175f;
    --band-fade: rgba(160, 20, 90, 0);
    --title-fill: #2a0a26;
  }
  * { margin: 0; padding: 0; box-sizing: border-box; }
  html, body { width: 930px; height: 1200px; overflow: hidden; background: var(--bg-deep); }
  .poster {
    position: relative;
    width: 930px;
    height: 1200px;
    overflow: hidden;
    font-family: "Pathway Gothic One", "Arial Narrow", sans-serif;
    color: var(--pink-text);
    background:
      radial-gradient(ellipse 520px 260px at 470px 260px, rgba(110, 25, 100, 0.55), transparent 75%),
      radial-gradient(ellipse 700px 600px at 420px 700px, var(--bg-glow), transparent 80%),
      linear-gradient(180deg, var(--bg-mid) 0%, var(--bg-deep) 100%);
  }
  .presenter {
    position: absolute;
    top: 40px; left: 0; width: 930px;
    text-align: center;
    font-size: 35px;
    color: var(--pink-soft);
  }
  .headliner {
    position: absolute;
    left: 112px; top: 120px;
    font-family: "Anton", "Impact", sans-serif;
    font-weight: normal;
    color: var(--title-fill);
    text-shadow: 0 0 2px var(--neon), 0 0 8px var(--neon), 0 0 22px rgba(255, 61, 187, 0.7);
    -webkit-text-stroke: 2px #ff7fd2;
    line-height: 1;
  }
  .headliner .prefix { display: block; font-size: 72px; margin-left: 8px; }
  .headliner .name { display: block; font-size: 200px; letter-spacing: 6px; margin-top: -22px; }
  .dj-portrait {
    position: absolute;
    left: 0; top: 410px;
    width: 600px; height: 790px;
    background:
      radial-gradient(ellipse 170px 230px at 245px 190px, #c25aa8, transparent 80%),
      radial-gradient(ellipse 330px 380px at 280px 620px, #4a1344, transparent 85%);
  }
  .event-info { position: absolute; right: 88px; text-align: right; }
  .date { top: 444px; font-size: 56px; line-height: 1.1; }
  .date .day { font-size: 74px; font-family: "Anton", sans-serif; margin: 0 14px; }
  .tagline { top: 540px; font-size: 38px; }
  .genres {
    top: 588px;
    font-size: 84px;
    line-height: 0.84;
    color: #fbe3f1;
    text-shadow: 0 0 6px var(--neon), 0 0 16px rgba(255, 61, 187, 0.6);
  }
  .catch-band {
    position: absolute;
    left: 425px; top: 762px;
    width: 560px; height: 162px;
    background: linear-gradient(90deg, var(--band-fade) 0%, var(--band-strong) 18%, var(--band-strong) 100%);
    transform: rotate(-2deg);
  }
  .catchphrase {
    position: absolute;
    left: 540px; top: 784px; width: 390px;
    text-align: center;
    font-size: 54px; line-height: 1.0;
    color: #fbd9ec;
  }
  .social { top: 944px; font-size: 20px; color: var(--pink-soft); }
  .social strong { color: var(--pink-text); font-weight: normal; }
  .venue-mark {
    position: absolute;
    right: 82px; top: 1052px;
    display: flex; align-items: center; gap: 10px;
    font-size: 30px; color: var(--pink-text);
  }
  .venue-mark .dot { width: 20px; height: 20px; border-radius: 50%; background: var(--pink-text); }
  .website { top: 1138px; right: 80px; font-size: 22px; }
</style>
</head>
<body>
  <main class="poster">
    <p class="presenter">Kell Cousins Sports Bar and Tap House presents</p>

    <h1 class="headliner"><span class="prefix">DJ</span><span class="name">PIVWHIRL</span></h1>

    <div class="dj-portrait" role="img" aria-label="Painted portrait of DJ Pivwhirl wearing headphones, sunglasses and a branded t-shirt, lit in magenta"></div>

    <p class="event-info date">Friday, July<span class="day">6th</span>2012</p>
    <p class="event-info tagline">Bringing you the best in</p>
    <p class="event-info genres">TOP 40, RETRO<br>AND FUNK</p>

    <div class="catch-band"></div>
    <p class="catchphrase">It's gonna be a<br>PIVWHIRL</p>

    <p class="event-info social">clubwall/chirpline: <strong>DJ Pivwhirl</strong></p>

    <div class="venue-mark"><span class="dot"></span>Kell Cousins</div>

    <p class="event-info website">www.thekellcousins.example</p>
  </main>
</body>
</html>
```